'Cradle Ahead' promotional brochure

We have designed a 6 week program to educate impending first-time parents about the things they need to know to survive the first 6 months. Sessions delivered by general practitioner/family doctor, dietician, physiotherapist, speech pathologist and psychologist. Our promotional blurb is: 'A comprehensive education program for first-time parents-to-be, delivered over 6 weeks by health professionals in your community, about everything you need to know to look after your baby (and yourself!) in the first 6 months'. I now want to put together a promotional brochure to be distributed to those couples who express an interest which will provide further details of what will be delivered in the course.
Updates
In terms of layout, I envisaged a double sided A4 size, foldable into 3 sections, but very happy to be guided on this.
Target Market(s)
To appeal to a young, well educated demographic. First time parents couples.
Industry/Entity Type
Medical
Font styles to use
Other font styles liked:
- Playfair Display
Requirements
Must have
- Playfair display font to be consistent with our logo (attached). Logo also included please. Some consistency with colours of logo please.
Nice to have
- I am a doctor, and have no creative genes! But prefer a clean and professional appearance overall. Not too cluttered in overall appearance.
Should not have
- No cheesy pictures of babies.

```html
<!DOCTYPE html>
<html lang="en">
<head>
<meta charset="utf-8">
<title>Cradle Ahead – Program Brochure</title>
<link rel="stylesheet" href="https://fonts.googleapis.com/css2?family=Montserrat:wght@500;600;700&family=Open+Sans:wght@400;700&display=swap">
<style>
  :root {
    --green: #5dba2f;
    --green-light: #7ccf45;
    --green-dark: #2f8f2c;
    --charcoal: #474749;
    --backdrop: #3b3b3d;
    --ink: #3a3a3a;
    --white: #ffffff;
  }
  * { box-sizing: border-box; margin: 0; padding: 0; }
  html, body { width: 801px; height: 1200px; overflow: hidden; }
  body { background: var(--backdrop); font-family: "Open Sans", Arial, sans-serif; color: var(--ink); position: relative; }

  .spread { position: absolute; left: 64px; width: 673px; height: 475px; overflow: hidden; background: linear-gradient(90deg, #fff 0%, #f3f3f3 50%, #e6e6e6 62%, #fff 63%, #fff 100%); }
  .spread--outside { top: 95px; }
  .spread--inside { top: 630px; background: linear-gradient(90deg, #fff 0%, #f2f2f2 40%, #fff 100%); }
  .spread__shapes { position: absolute; inset: 0; }

  .week { position: absolute; font-family: "Montserrat", Arial, sans-serif; font-weight: 600; font-size: 23px; line-height: 1; }
  .week__arrow { display: inline-block; width: 10px; height: 15px; vertical-align: -1px; }
  .week--light { color: var(--white); }
  .week--dark { color: var(--charcoal); }

  .copy { position: absolute; font-size: 7.6px; line-height: 1.38; }
  .copy p + p { margin-top: 8px; }
  .copy b { font-weight: 700; }
  .copy--light { color: var(--white); }
  .copy--right { text-align: right; }

  .ticks { list-style: none; margin-top: 10px; }
  .ticks li { position: relative; padding-left: 17px; line-height: 1.42; }
  .ticks li::before { content: ""; position: absolute; left: 2px; top: 2px; width: 3px; height: 6px; border: solid var(--green); border-width: 0 2px 2px 0; transform: rotate(40deg); }
  .ticks--right li { padding-left: 0; padding-right: 15px; }
  .ticks--right li::before { left: auto; right: 3px; border-color: var(--white); }

  .title { position: absolute; right: 44px; top: 36px; font-family: "Montserrat", Arial, sans-serif; font-weight: 600; font-size: 35px; color: var(--white); letter-spacing: -0.5px; }

  .clinic { position: absolute; display: flex; align-items: center; gap: 10px; font-family: "Montserrat", Arial, sans-serif; font-weight: 600; color: var(--charcoal); text-transform: uppercase; line-height: 1.1; }
  .clinic__mark { background: var(--green); flex: none; }
  .clinic--large { left: 405px; top: 140px; font-size: 17px; }
  .clinic--large .clinic__mark { width: 40px; height: 40px; }
  .clinic--small { left: 22px; top: 364px; font-size: 12px; }
  .clinic--small .clinic__mark { width: 30px; height: 30px; }

  .contact { position: absolute; left: 0; width: 336px; top: 428px; text-align: center; color: var(--white); font-family: "Montserrat", Arial, sans-serif; }
  .contact__label { font-size: 10.5px; font-weight: 600; }
  .contact__phone { font-size: 19px; font-weight: 600; margin-top: 1px; }
</style>
</head>
<body>

<section class="spread spread--outside">
  <svg class="spread__shapes" viewBox="0 0 673 475" width="673" height="475">
    <defs>
      <linearGradient id="outGreen" x1="0" y1="0" x2="1" y2="0">
        <stop offset="0" stop-color="#3f9f2c"/><stop offset="1" stop-color="#6cc63a"/>
      </linearGradient>
      <linearGradient id="monoHands" x1="0" y1="0" x2="1" y2="1">
        <stop offset="0" stop-color="#c9c9c9"/><stop offset="0.5" stop-color="#8a8a8a"/><stop offset="1" stop-color="#2a2a2a"/>
      </linearGradient>
      <linearGradient id="lakeScene" x1="0" y1="0" x2="0" y2="1">
        <stop offset="0" stop-color="#7d7a3a"/><stop offset="0.55" stop-color="#4c6fa8"/><stop offset="1" stop-color="#8a7a68"/>
      </linearGradient>
    </defs>
    <path d="M0 0 H673 V135 C600 110 520 92 420 108 C300 128 230 190 160 183 C90 176 40 160 0 152 Z" fill="url(#outGreen)"/>
    <path d="M0 152 C40 160 90 176 160 183 C230 190 300 128 420 108 C520 92 600 110 673 135" fill="none" stroke="var(--charcoal)" stroke-width="9"/>
    <rect x="0" y="418" width="673" height="57" fill="var(--green)"/>
    <circle cx="690" cy="560" r="252" fill="var(--green-dark)"/>
    <circle cx="690" cy="560" r="244" fill="url(#monoHands)" role="img" aria-label="Black and white photo of a parent's hands cradling a baby's hand"/>
    <circle cx="306" cy="287" r="89" fill="var(--green-dark)"/>
    <circle cx="306" cy="287" r="81" fill="url(#lakeScene)" role="img" aria-label="Photo of an expectant mother relaxing on a lakeside jetty"/>
  </svg>

  <div class="title">“Cradle Ahead”</div>

  <h2 class="week week--light" style="left:22px;top:34px"><svg class="week__arrow" viewBox="0 0 10 15"><path d="M2 2 L8 7.5 L2 13" fill="none" stroke="currentColor" stroke-width="2.6"/></svg> Week 5</h2>
  <div class="copy copy--light" style="left:23px;top:68px;width:245px">
    <p><b>Session 1</b> – Clinical Psychologist Dr Mara Ellison will share information about bonding &amp; attachment with your baby, how to promote their social &amp; emotional development and how to manage separation anxiety. She will also discuss positive parenting approaches.</p>
  </div>

  <h2 class="week week--dark" style="left:22px;top:199px"><svg class="week__arrow" viewBox="0 0 10 15"><path d="M2 2 L8 7.5 L2 13" fill="none" stroke="currentColor" stroke-width="2.6"/></svg> Week 6</h2>
  <div class="copy" style="left:23px;top:231px;width:162px">
    <p><b>Session 1</b> – Secret Men's Business – a men-only session (including beer!) with a new father for frank discussion about the road ahead. Mums will do a shopping excursion with the GP &amp; Dietician to FreshMart to look at baby products and food – the good and the bad!</p>
    <p><b>Session 2</b> – Program review, reflection and evaluation and future session planning when baby is 6 months of age.</p>
  </div>

  <div class="clinic clinic--small"><span class="clinic__mark"></span><span>Banksia<br>Family<br>Clinic</span></div>
  <div class="clinic clinic--large"><span class="clinic__mark"></span><span>Banksia<br>Family<br>Clinic</span></div>

  <div class="contact">
    <div class="contact__label">Contact Details for Enquiries/Bookings</div>
    <div class="contact__phone">(02) 5550 1234</div>
  </div>
</section>

<section class="spread spread--inside">
  <svg class="spread__shapes" viewBox="0 0 673 475" width="673" height="475">
    <defs>
      <linearGradient id="inGreen" x1="0" y1="0" x2="1" y2="1">
        <stop offset="0" stop-color="#6cc63a"/><stop offset="1" stop-color="#4fae2c"/>
      </linearGradient>
      <linearGradient id="bellyHands" x1="0" y1="0" x2="1" y2="0">
        <stop offset="0" stop-color="#e8e6e8"/><stop offset="0.6" stop-color="#d7c8c4"/><stop offset="1" stop-color="#eef2f5"/>
      </linearGradient>
      <radialGradient id="skin" cx="0.5" cy="0.45" r="0.6">
        <stop offset="0" stop-color="#e2b79a"/><stop offset="1" stop-color="#b98366"/>
      </radialGradient>
      <radialGradient id="babyHands" cx="0.4" cy="0.5" r="0.6">
        <stop offset="0" stop-color="#f4d6c6"/><stop offset="1" stop-color="#e3b3a0"/>
      </radialGradient>
    </defs>
    <rect x="335" y="0" width="338" height="140" fill="url(#bellyHands)" role="img" aria-label="Photo of hands resting on a pregnant belly"/>
    <path d="M0 295 C110 293 200 285 270 230 C330 180 360 160 420 135 C520 100 620 98 673 100 V475 H0 Z" fill="url(#inGreen)"/>
    <path d="M0 295 C110 293 200 285 270 230 C330 180 360 160 420 135 C520 100 620 98 673 100" fill="none" stroke="var(--charcoal)" stroke-width="9"/>
    <circle cx="240" cy="228" r="89" fill="var(--green-dark)"/>
    <circle cx="240" cy="228" r="81" fill="url(#skin)" role="img" aria-label="Photo of hands forming a heart shape on a bare belly"/>
    <circle cx="430" cy="416" r="82" fill="var(--charcoal)"/>
    <circle cx="430" cy="416" r="74" fill="url(#babyHands)" role="img" aria-label="Photo of a parent's hand holding a sleeping newborn's hand"/>
  </svg>

  <h2 class="week week--dark" style="left:22px;top:40px"><svg class="week__arrow" viewBox="0 0 10 15"><path d="M2 2 L8 7.5 L2 13" fill="none" stroke="currentColor" stroke-width="2.6"/></svg> Week 1</h2>
  <div class="copy" style="left:23px;top:71px;width:270px">
    <p>GP Dr Helen Ashby will share information for Mum's own health after delivery. Topics include:</p>
    <ul class="ticks">
      <li>Vaccinations in pregnancy</li>
      <li>Bleeding, bladder and bowel after delivery</li>
      <li>Breastfeeding, engorgement and mastitis</li>
      <li>Bottle feeding</li>
      <li>Post-natal anxiety &amp; depression</li>
      <li>Intimacy and contraception</li>
    </ul>
  </div>

  <h2 class="week week--light" style="left:22px;top:320px"><svg class="week__arrow" viewBox="0 0 10 15"><path d="M2 2 L8 7.5 L2 13" fill="none" stroke="currentColor" stroke-width="2.6"/></svg> Week 2</h2>
  <div class="copy copy--light" style="left:23px;top:352px;width:290px">
    <p><b>Session 1</b> – Clinical Psychologist Dr Mara Ellison will discuss changes in relationships as couples becomes parents, gender roles in parenting and post natal depression.</p>
    <p><b>Session 2</b> – Physiotherapist Ruth Calder will present advice for Mums regarding exercise during and after pregnancy, looking after the pelvic floor during and after pregnancy, and abdominal muscle separation management. She will also provide advice for promoting babies' neck strength and minimising the risk of flat spots on the head and encouraging gross motor skills in the first 6 months</p>
  </div>

  <h2 class="week week--light" style="right:17px;top:135px">Week 3 <svg class="week__arrow" viewBox="0 0 10 15"><path d="M8 2 L2 7.5 L8 13" fill="none" stroke="currentColor" stroke-width="2.6"/></svg></h2>
  <div class="copy copy--light copy--right" style="right:17px;top:168px;width:290px">
    <p>Session 1 – Dietician Nora Whitfield provides advice for Mums regarding healthy eating during pregnancy and lactation, normal weight gain during pregnancy and realistic weight loss after. She will also discuss the evidence regarding breastfeeding VS bottle-feeding, normal infant weight gain and introducing solids (including those with potential for allergy).</p>
    <p>Session 2 – Paediatric Speech Pathologist Tess Lowry will share information about latching and breast-feeding troubles &amp; tongue tie, advice about dummies and finger-sucking, introducing solids &amp; feeding (including 'pouch' food), encouraging language development and current evidence about electronic devices impacting language development.</p>
  </div>

  <h2 class="week week--light" style="right:17px;top:306px">Week 4 <svg class="week__arrow" viewBox="0 0 10 15"><path d="M8 2 L2 7.5 L8 13" fill="none" stroke="currentColor" stroke-width="2.6"/></svg></h2>
  <div class="copy copy--light copy--right" style="right:17px;top:337px;width:160px">
    <p>GP Dr Helen Ashby will share advice about your babies' health in the first 6 months, including:</p>
    <ul class="ticks ticks--right">
      <li>Skin of newborns</li>
      <li>Sleeping</li>
      <li>Crying</li>
      <li>Immunisations</li>
      <li>Fever and infections</li>
      <li>Diarrhoea and constipation</li>
      <li>Teething</li>
      <li>Understanding a baby's signals</li>
    </ul>
  </div>
</section>

</body>
</html>
```